Vornel Technologies business card design

We need a business card designed with our new logo. it would be great if the card could communicate it is a technology based company.

Target Market(s)

system integrators

Industry/Entity Type

technology, IOT

Contact Information for Business Card

Name, designation, Address, telephone number, email address

Requirements
Must have
• logo and company name
Nice to have
• something to do with technology

```html
<!DOCTYPE html>
<html lang="en">
<head>
<meta charset="utf-8">
<title>Vornel Technologies – Business Card</title>
<link rel="stylesheet" href="https://fonts.googleapis.com/css2?family=Open+Sans:wght@400;600;700&display=swap">
<style>
  :root {
    --page-bg: #e7e4df;
    --card-dark: #1d1c20;
    --card-dark-2: #2b2a30;
    --card-light: #f4f4f6;
    --card-light-2: #d9d9de;
    --glow-violet: #5b4f86;
    --glow-lilac: #b9b3d8;
    --ink-dark: #3a3a3e;
    --ink-mid: #55555a;
    --accent: #f2a92c;
    --white: #ffffff;
  }
  * { margin: 0; padding: 0; box-sizing: border-box; }
  html, body {
    width: 1200px; height: 1023px; overflow: hidden;
    background: var(--page-bg);
    font-family: "Open Sans", Arial, sans-serif;
  }
  .card {
    position: absolute; left: 180px;
    width: 840px; height: 480px;
    border-radius: 6px; overflow: hidden;
    box-shadow: 0 6px 18px rgba(0,0,0,.18);
  }
  .card--front {
    top: 26px;
    background: linear-gradient(160deg, var(--card-dark-2) 0%, var(--card-dark) 60%);
  }
  .card--back {
    top: 522px;
    background: linear-gradient(200deg, var(--card-light) 30%, var(--card-light-2) 100%);
  }
  .tech-backdrop { position: absolute; }
  .card--front .tech-backdrop {
    left: 0; bottom: 0; width: 100%; height: 60%;
    background: radial-gradient(ellipse at 20% 95%, rgba(91,79,134,.75) 0%, rgba(60,52,92,.45) 40%, rgba(29,28,32,0) 75%);
  }
  .card--back .tech-backdrop {
    left: 0; top: 0; width: 100%; height: 55%;
    background: radial-gradient(ellipse at 30% 0%, rgba(91,79,134,.55) 0%, rgba(185,179,216,.4) 45%, rgba(244,244,246,0) 80%);
  }
  .brand {
    position: absolute; display: flex; align-items: center; gap: 18px;
  }
  .brand__mark { width: 44px; height: 44px; background: var(--accent); flex: none; }
  .brand__name {
    font-weight: 700; font-size: 54px; line-height: 1; letter-spacing: 1px;
    text-transform: uppercase;
  }
  .card--front .brand { left: 0; right: 0; top: 196px; justify-content: center; }
  .card--front .brand__name { color: var(--white); }
  .card--back .brand { right: 48px; top: 150px; }
  .card--back .brand__mark { width: 34px; height: 34px; }
  .card--back .brand__name { color: var(--ink-dark); font-size: 40px; }
  .contact { position: absolute; left: 330px; top: 250px; color: var(--ink-mid); }
  .contact__name { font-weight: 700; font-size: 24px; color: var(--ink-dark); }
  .contact__role { font-size: 15px; color: var(--accent); margin-bottom: 10px; }
  .contact__address { font-size: 15px; line-height: 1.45; margin-bottom: 8px; }
  .contact__list { list-style: none; font-size: 15px; line-height: 1.6; }
  .contact__list li { display: flex; align-items: center; gap: 10px; }
  .contact__icon { width: 14px; height: 14px; flex: none; fill: none; stroke: var(--accent); stroke-width: 2; }
</style>
</head>
<body>
  <section class="card card--front" aria-label="Card front">
    <div class="tech-backdrop" role="img" aria-label="Soft violet glow of abstract network polygons and light points"></div>
    <div class="brand">
      <span class="brand__mark"></span>
      <span class="brand__name">Vornel Technologies</span>
    </div>
  </section>

  <section class="card card--back" aria-label="Card back">
    <div class="tech-backdrop" role="img" aria-label="Soft lilac glow of abstract network polygons and light points"></div>
    <div class="brand">
      <span class="brand__mark"></span>
      <span class="brand__name">Vornel Technologies</span>
    </div>
    <div class="contact">
      <p class="contact__name">Your Name Here</p>
      <p class="contact__role">Managing Director</p>
      <p class="contact__address">4415 Carrow Mesa Dr,<br>#210 Larkfield, Nevada 89417</p>
      <ul class="contact__list">
        <li><svg class="contact__icon" viewBox="0 0 16 16"><path d="M3 2h3l1.5 3.5-2 1.2a8 8 0 0 0 3.8 3.8l1.2-2L14 10v3a1 1 0 0 1-1 1A11 11 0 0 1 2 3a1 1 0 0 1 1-1z"/></svg>(555) 482-1907</li>
        <li><svg class="contact__icon" viewBox="0 0 16 16"><rect x="4" y="1.5" width="8" height="13" rx="1.5"/><line x1="7" y1="12" x2="9" y2="12"/></svg>(555) 482-1907</li>
        <li><svg class="contact__icon" viewBox="0 0 16 16"><rect x="1.5" y="3.5" width="13" height="9" rx="1"/><path d="M1.5 4l6.5 5 6.5-5"/></svg>youremail@youremail.com</li>
        <li><svg class="contact__icon" viewBox="0 0 16 16"><circle cx="8" cy="8" r="6.5"/><path d="M1.5 8h13M8 1.5c2.5 2.5 2.5 10.5 0 13M8 1.5c-2.5 2.5-2.5 10.5 0 13"/></svg>www.yourwebsite.com</li>
      </ul>
    </div>
  </section>
</body>
</html>
```